Business Card Design needed for logo design project

This project is linked to Logo: brand identity for modern furniture design studio..

Our company needs a Business Card Design. Please refer to our original project in the link above.

Industry/Entity Type

Business

```html
<!DOCTYPE html>
<html lang="en">
<head>
<meta charset="utf-8">
<title>vanto business card</title>
<link rel="stylesheet" href="https://fonts.googleapis.com/css2?family=Quicksand:wght@400&family=Bebas+Neue&family=Arimo:wght@400&display=swap">
<style>
  :root {
    --bg: #ecebe8;
    --card-grey: #525252;
    --card-white: #ffffff;
    --text-light: #ffffff;
    --text-muted: #b9b9b9;
    --text-dark: #3c3c3c;
    --label: #6a6a6a;
  }
  * { margin: 0; padding: 0; box-sizing: border-box; }
  html, body { width: 1200px; height: 835px; overflow: hidden; background: var(--bg); }
  .canvas { position: relative; width: 1200px; height: 835px; }

  .card {
    position: absolute;
    width: 539px; height: 329px;
    border-radius: 18px;
    overflow: hidden;
    background: var(--card-grey);
  }
  .card--front { left: 118px; top: 63px; }
  .card--back  { left: 535px; top: 412px; }

  .white-strip { position: absolute; left: 0; top: 0; bottom: 0; background: var(--card-white); }
  .card--front .white-strip { width: 142px; }
  .card--back .white-strip { width: 160px; }

  .web-address {
    position: absolute; left: 71px; top: 164px;
    transform: translate(-50%, -50%) rotate(-90deg);
    font-family: "Arimo", sans-serif; font-size: 15px; color: var(--text-dark);
    white-space: nowrap; letter-spacing: 0.3px;
  }
  .brand-name {
    position: absolute; left: 341px; top: 160px;
    transform: translate(-50%, -50%);
    font-family: "Quicksand", sans-serif; font-weight: 400;
    font-size: 86px; color: var(--text-light); letter-spacing: 1px; line-height: 1;
  }

  .brand-bar {
    position: absolute; left: 54px; top: 0; width: 52px; height: 213px;
    background: var(--card-grey);
  }
  .brand-bar__name {
    position: absolute; left: 26px; top: 108px;
    transform: translate(-50%, -50%) rotate(90deg);
    font-family: "Quicksand", sans-serif; font-weight: 400;
    font-size: 46px; color: var(--text-light); line-height: 1; white-space: nowrap;
  }

  .contact-block { position: absolute; left: 259px; top: 92px; font-family: "Arimo", sans-serif; }
  .person-name { font-family: "Bebas Neue", sans-serif; font-size: 25px; color: var(--text-light); line-height: 1; letter-spacing: 0.3px; }
  .person-role { font-size: 15px; color: var(--text-muted); margin-top: 2px; }
  .contact-list { list-style: none; margin-top: 28px; }
  .contact-list li { display: flex; align-items: center; height: 27.5px; font-size: 16px; color: var(--text-light); }
  .contact-icon { width: 21px; height: 21px; margin-right: 7px; flex: none; }

  .side-label {
    position: absolute; font-family: "Arimo", sans-serif; font-size: 36px; color: var(--label);
  }
  .side-label--front { left: 238px; top: 407px; }
  .side-label--back { left: 683px; top: 758px; }
</style>
</head>
<body>
<main class="canvas">
  <section class="card card--front" aria-label="Card front">
    <div class="white-strip"></div>
    <span class="web-address">www.vanto.com</span>
    <span class="brand-name">vanto</span>
  </section>
  <p class="side-label side-label--front">Front Side</p>

  <section class="card card--back" aria-label="Card back">
    <div class="white-strip">
      <div class="brand-bar"><span class="brand-bar__name">vanto</span></div>
    </div>
    <div class="contact-block">
      <p class="person-name">PERSON NAME</p>
      <p class="person-role">Managing Director</p>
      <ul class="contact-list">
        <li>
          <svg class="contact-icon" viewBox="0 0 21 21" aria-hidden="true">
            <circle cx="10.5" cy="10.5" r="9.5" fill="none" stroke="#fff" stroke-width="1.6"/>
            <path d="M7 5.5l2 2.2-1.1 1.4c.7 1.5 1.9 2.7 3.4 3.4l1.4-1.1 2.2 2-1.2 1.6c-3.8-.4-7.3-3.9-7.7-7.7z" fill="#fff"/>
          </svg>555 210 4870</li>
        <li>
          <svg class="contact-icon" viewBox="0 0 21 21" aria-hidden="true">
            <circle cx="10.5" cy="10.5" r="9.5" fill="none" stroke="#fff" stroke-width="1.6"/>
            <rect x="5.5" y="7" width="10" height="7" fill="none" stroke="#fff" stroke-width="1.3"/>
            <path d="M5.5 7l5 4 5-4" fill="none" stroke="#fff" stroke-width="1.3"/>
          </svg>hello@vanto.com</li>
        <li>
          <svg class="contact-icon" viewBox="0 0 21 21" aria-hidden="true">
            <circle cx="10.5" cy="10.5" r="9.5" fill="none" stroke="#fff" stroke-width="1.6"/>
          </svg>social.link/name</li>
        <li>
          <svg class="contact-icon" viewBox="0 0 21 21" aria-hidden="true">
            <circle cx="10.5" cy="10.5" r="9.5" fill="none" stroke="#fff" stroke-width="1.6"/>
          </svg>feed.link/name</li>
      </ul>
    </div>
  </section>
  <p class="side-label side-label--back">Back Side</p>
</main>
</body>
</html>
```